Tolvik cards

I want a simple business card that pops.
Logo on one side.
On side two i want.
"Are you thinking about a new building on your property, or renovating an existing structure? Contact".....
Owners Name: Gary Pellman
Owners Phone number: 555-209-4176
Address:4716 Copper Fern RD, Linford, PA 15571
Committed to Quality, Service, and Integrity

```html
<!DOCTYPE html>
<html lang="en">
<head>
<meta charset="utf-8">
<title>Tolvik Builders Business Card</title>
<link href="https://fonts.googleapis.com/css2?family=Poppins:wght@400;500;700;800&display=swap" rel="stylesheet">
<style>
  :root {
    --backdrop: #1f1f1f;
    --brown: #45301f;
    --brown-text: #3a2718;
    --icon-brown: #6b4a30;
    --white: #ffffff;
  }
  * { box-sizing: border-box; margin: 0; padding: 0; }
  html, body {
    width: 1200px; height: 1200px; overflow: hidden;
    background: var(--backdrop);
    font-family: "Poppins", sans-serif;
  }
  .stage {
    width: 1200px; height: 1200px;
    display: flex; flex-direction: column; align-items: center; justify-content: center;
    gap: 44px;
  }
  .card {
    width: 900px; height: 514px;
    position: relative; overflow: hidden;
    box-shadow: 0 18px 40px rgba(0,0,0,.55);
  }
  /* Front */
  .card-front {
    background: var(--brown);
    display: flex; align-items: center; justify-content: center; gap: 28px;
  }
  .brand-mark {
    width: 110px; height: 110px; background: var(--white);
  }
  .brand-name {
    color: var(--white); font-weight: 800; line-height: 1;
    display: flex; flex-direction: column;
  }
  .brand-name .brand-main { font-size: 104px; letter-spacing: 1px; }
  .brand-name .brand-sub { font-size: 30px; letter-spacing: 3px; margin-top: 6px; }
  /* Back */
  .card-back {
    background: var(--white); color: var(--brown-text);
    text-align: center;
  }
  .pitch {
    position: absolute; top: 96px; left: 0; right: 0;
    font-size: 25px; font-weight: 400; line-height: 1.35;
    padding: 0 70px;
  }
  .divider {
    position: absolute; top: 186px; left: 70px; right: 70px;
    height: 2px; background: var(--brown-text);
  }
  .owner-name {
    position: absolute; top: 212px; left: 0; right: 0;
    font-size: 33px; font-weight: 700; letter-spacing: .5px;
  }
  .contact-line {
    position: absolute; left: 0; right: 0;
    display: flex; align-items: center; justify-content: center; gap: 12px;
    font-size: 26px; font-weight: 500; letter-spacing: 1px;
  }
  .contact-phone { top: 268px; }
  .contact-address { top: 314px; }
  .contact-icon { width: 30px; height: 30px; flex: none; }
  .tagline-band {
    position: absolute; left: 0; right: 0; top: 392px; height: 80px;
    background: var(--brown); color: var(--white);
    display: flex; align-items: center; justify-content: center;
    font-size: 27px; font-weight: 500; letter-spacing: 3px;
  }
</style>
</head>
<body>
<main class="stage">
  <section class="card card-front" aria-label="Card front">
    <div class="brand-mark" aria-hidden="true"></div>
    <div class="brand-name">
      <span class="brand-main">TOLVIK</span>
      <span class="brand-sub">BUILDERS LLC</span>
    </div>
  </section>

  <section class="card card-back" aria-label="Card back">
    <p class="pitch">Are you thinking about a new building on your property,<br>or renovating an existing structure? Contact</p>
    <div class="divider"></div>
    <h1 class="owner-name">GARY PELLMAN</h1>
    <p class="contact-line contact-phone">
      <svg class="contact-icon" viewBox="0 0 30 30" aria-hidden="true">
        <circle cx="15" cy="15" r="15" fill="var(--icon-brown)"/>
        <path d="M11 8c1 0 2 3 2 4s-1 1.5-1 2 2 4 4 4.5c.5 0 1-1 2-1s3.5 1 3.5 2-1.5 3-3 3C13 22.5 8 17 8 11.5 8 10 10 8 11 8z" fill="#fff"/>
      </svg>
      555-209-4176
    </p>
    <p class="contact-line contact-address">
      <svg class="contact-icon" viewBox="0 0 30 30" aria-hidden="true">
        <circle cx="15" cy="15" r="15" fill="var(--icon-brown)"/>
        <path d="M15 7a5.5 5.5 0 0 1 5.5 5.5C20.5 17 15 23 15 23s-5.5-6-5.5-10.5A5.5 5.5 0 0 1 15 7z" fill="#fff"/>
        <circle cx="15" cy="12.5" r="2" fill="var(--icon-brown)"/>
      </svg>
      4716 Copper Fern RD, Linford, PA 15571
    </p>
    <div class="tagline-band">COMMITTED TO QUALITY | SERVICE | AND INTEGRITY</div>
  </section>
</main>
</body>
</html>
```